We Buy Houses Website

Looking for a highly motivated and skillfull designer to design and code me a "we Buy Houses" type website. I have a potential logo, but if you think you can make a BETTER one, please do try and incorporate it in your template. I am looking for creativity, professionalism, simple yet elegant. I will need a simple form on the front of the template along with pictures I provide you of recent houses I have bought. Look at these sites for examples of the layout of the website:

http://www.brickvalehomes.example/
http://www.petrafixeshouses.example/
http://www.quickpropertyexitnow.example/

If you make me a design that blows me away, and you are dependable, you will become part of my team and in charge of the web aspect which will include designing, updating, any and all graphics and logo work, SEO, coding. If you have skills in all of these areas please make me a design and lets do business!! The name of the website will be "Lurt Takes Homes" at LurtTakesHomes.example

I have uploaded some pictures of houses that we have done, please feel free to incorporate this into the banner or the design, etc. I want them to know we buy houses in ANY condition, as is, cash, can close immediately so they can get on with their life. We have many options to help them find a solution to whatever problem they have. We are in the business of helping people.

Target Market(s)

People looking to sell their houses
people facing foreclosure, bankruptcy, death in the family, divorce, anyone that we can help
people with ugly houses that need a lot of repair

Industry/Entity Type

Business

Font styles to use
Serif
Sans Serif

Colors

Designer to choose colors to be used in the design.

Requirements
Must have
• must have a simple form on the front of the page, preferrably near the banner, with the few required fields to help someone get started putting in their interest to sell their house, view the 2 websites i put as examples to see what kind of fields it should have.

My phone number (555) 482-1937 along with a Lurt Takes Homes logo, clean simple and elegant and professional. I want a nice color scheme that is not white but professional and has a wow factor.

```html
<!DOCTYPE html>
<html lang="en">
<head>
<meta charset="utf-8">
<title>Home – Lurt Takes Homes</title>
<link rel="stylesheet" href="https://fonts.googleapis.com/css2?family=Raleway:wght@300;400;600;700;800&family=Lora:ital@1&display=swap">
<style>
  :root {
    --navy: #050b1e;
    --navy-glass: rgba(8, 14, 40, 0.86);
    --lime: #c4f02a;
    --field: #efefef;
    --placeholder: #a9a9a9;
    --sky-top: #3b6fd4;
    --sky-low: #7fa8e8;
    --lawn: #4f8a3a;
    --white: #ffffff;
    --tweet-name: #2a6fb8;
    --tweet-meta: #9a9a9a;
    --tweet-text: #333333;
  }
  * { box-sizing: border-box; margin: 0; padding: 0; }
  html, body { width: 1200px; height: 675px; overflow: hidden; }
  body {
    position: relative;
    font-family: "Raleway", Arial, sans-serif;
    background: var(--sky-top);
  }
  .hero-photo {
    position: absolute; inset: 0;
    background: linear-gradient(180deg, var(--sky-top) 0%, var(--sky-low) 45%, #c9c2b0 62%, #8f8a7c 75%, var(--lawn) 85%, #3f7430 100%);
  }
  .site-header {
    position: absolute; left: 0; top: 95px; width: 1200px; height: 55px;
    background: var(--navy);
  }
  .header-accent {
    position: absolute; left: 0; top: 0; width: 35px; height: 55px;
    background: var(--lime);
  }
  .brand {
    position: absolute; left: 238px; top: 0; height: 55px;
    display: flex; align-items: center; gap: 6px;
    color: var(--lime); font-weight: 700; font-size: 13px; letter-spacing: .3px;
  }
  .brand-mark { width: 10px; height: 10px; background: var(--lime); }
  .main-nav { position: absolute; left: 629px; top: 0; display: flex; height: 55px; }
  .main-nav a {
    display: flex; align-items: center; justify-content: center;
    height: 55px; color: var(--white); text-decoration: none;
    font-size: 10px; font-weight: 800; letter-spacing: -.1px;
  }
  .main-nav a.is-active { background: var(--lime); color: var(--navy); width: 88px; }
  .main-nav .n2 { width: 94px; } .main-nav .n3 { width: 90px; }
  .main-nav .n4 { width: 88px; } .main-nav .n5 { width: 100px; } .main-nav .n6 { width: 90px; }

  .lead-form {
    position: absolute; left: 205px; top: 202px; width: 286px; height: 378px;
    background: var(--navy-glass); border-radius: 12px;
    padding-top: 20px; text-align: center;
  }
  .lead-form label {
    display: block; color: var(--lime); font-weight: 700; font-size: 12px;
    text-transform: uppercase; margin-bottom: 6px;
  }
  .lead-form .field {
    display: block; width: 214px; height: 18px; margin: 0 0 14px 35px;
    background: var(--field); border: 0; padding-left: 4px;
    font-family: "Lora", Georgia, serif; font-style: italic; font-size: 9px;
    color: var(--placeholder); text-align: left; line-height: 18px;
  }
  .lead-form .submit {
    display: block; margin: 12px auto 0; width: 102px; height: 23px;
    background: var(--lime); border: 0; border-radius: 5px;
    font-family: "Raleway", Arial, sans-serif; font-weight: 700; font-size: 12px; color: var(--navy);
  }

  .news-panel {
    position: absolute; left: 678px; top: 255px; width: 304px; height: 297px;
    background: var(--navy-glass); border-radius: 12px;
  }
  .news-title {
    position: absolute; left: 50px; top: 16px;
    color: var(--lime); font-weight: 600; font-size: 40px; letter-spacing: -.5px; line-height: 1;
  }
  .news-add { position: absolute; left: 257px; top: 24px; width: 28px; height: 28px; }
  .tweet-feed {
    position: absolute; left: 52px; top: 53px; width: 205px; height: 205px;
    background: var(--white); padding: 9px 6px 0;
  }
  .tweet { display: flex; gap: 5px; height: 31px; }
  .tweet-avatar { width: 20px; height: 20px; background: #8a7a66; flex: none; }
  .tweet-body { font-family: Arial, Helvetica, sans-serif; font-size: 6.5px; line-height: 8px; }
  .tweet-name { color: var(--tweet-name); font-weight: 700; }
  .tweet-handle { color: var(--tweet-meta); font-weight: 400; font-size: 5px; }
  .tweet-text { color: var(--tweet-text); font-size: 6px; line-height: 7px; }
  .tweet-meta { color: var(--tweet-meta); font-size: 5px; word-spacing: 4px; }
</style>
</head>
<body>
  <div class="hero-photo" role="img" aria-label="Photo of a single-storey house with garage, driveway and green lawn under a clear blue sky"></div>

  <header class="site-header">
    <div class="header-accent"></div>
    <div class="brand"><span class="brand-mark"></span>Lurt Takes Homes</div>
    <nav class="main-nav">
      <a class="is-active" href="#">HOME</a>
      <a class="n2" href="#">HOW IT WORKS</a>
      <a class="n3" href="#">INVESTORS</a>
      <a class="n4" href="#">SELL YOUR HOUSE</a>
      <a class="n5" href="#">RECENT PROJECTS</a>
      <a class="n6" href="#">ABOUT ME</a>
    </nav>
  </header>

  <form class="lead-form">
    <label>First Name:</label><span class="field">Enter Name</span>
    <label>Last Name:</label><span class="field">Enter Your Message</span>
    <label>Phone Number:</label><span class="field">Enter Your Message</span>
    <label>Email:</label><span class="field">Enter Email</span>
    <label>Property Address:</label><span class="field">Enter Address</span>
    <label>Zip Code:</label><span class="field">Enter Zip</span>
    <button class="submit" type="button">GET INFO</button>
  </form>

  <section class="news-panel">
    <h2 class="news-title">NEWS</h2>
    <svg class="news-add" viewBox="0 0 28 28" aria-hidden="true">
      <rect x="12" y="0" width="4" height="28" fill="#c4f02a"/>
      <rect x="0" y="12" width="28" height="4" fill="#c4f02a"/>
    </svg>
    <div class="tweet-feed">
      <div class="tweet"><div class="tweet-avatar"></div><div class="tweet-body"><div class="tweet-name">Marlo Penfield <span class="tweet-handle">@marlopenfield</span></div><div class="tweet-text">working too late</div><div class="tweet-meta">7 years ago Reply Retweet Favorite</div></div></div>
      <div class="tweet"><div class="tweet-avatar"></div><div class="tweet-body"><div class="tweet-name">Marlo Penfield <span class="tweet-handle">@marlopenfield</span></div><div class="tweet-text">going to sleep</div><div class="tweet-meta">7 years ago Reply Retweet Favorite</div></div></div>
      <div class="tweet"><div class="tweet-avatar"></div><div class="tweet-body"><div class="tweet-name">Marlo Penfield <span class="tweet-handle">@marlopenfield</span></div><div class="tweet-text">going to the moon</div><div class="tweet-meta">7 years ago Reply Retweet Favorite</div></div></div>
      <div class="tweet"><div class="tweet-avatar"></div><div class="tweet-body"><div class="tweet-name">Marlo Penfield <span class="tweet-handle">@marlopenfield</span></div><div class="tweet-text">going to sleep</div><div class="tweet-meta">7 years ago Reply Retweet Favorite</div></div></div>
      <div class="tweet"><div class="tweet-avatar"></div><div class="tweet-body"><div class="tweet-name">Marlo Penfield <span class="tweet-handle">@marlopenfield</span></div><div class="tweet-text">awake, at work and moving along</div><div class="tweet-meta">7 years ago Reply Retweet Favorite</div></div></div>
      <div class="tweet"><div class="tweet-avatar"></div><div class="tweet-body"><div class="tweet-name">Marlo Penfield <span class="tweet-handle">@marlopenfield</span></div><div class="tweet-text">now back at work for a fresh new week. let's see what's happening</div><div class="tweet-meta">7 years ago Reply Retweet Favorite</div></div></div>
    </div>
  </section>
</body>
</html>
```